Webdesign für Gebäudereinigung
Zielgruppe
Seit 2005 ist LUM Dienstleistungen der Partner für Gebäudereinigung in Berlin. Wir haben Firmenkunden sowie privat Kunden und kümmern uns um sämtliche Reinigungen. Wie Glasreinigung, Büro- und Unterhaltungsreinigung, Bau- und Baufeinreinigung, Aufgangsreinigung & Grundreinigung…
Aufgabenstellung
Unsere neue Webseite sollte modern - Zeitlos - freundlich sein … Farben am Logo orientieren, das übernehmen wir weiterhin….

```html
<!DOCTYPE html>
<html lang="en">
<head>
<meta charset="utf-8">
<title>LUM Dienstleistungen – Office cleaning in Berlin</title>
<link href="https://fonts.googleapis.com/css2?family=Work+Sans:wght@400;500;600;700&family=Oswald:wght@300;400&display=swap" rel="stylesheet">
<style>
:root{
  --navy:#0b2463;
  --navy-deep:#082a5a;
  --yellow:#ffd400;
  --teal:#2ba8a8;
  --teal-text:#2a9fa3;
  --mist:#e4eaed;
  --paper:#ffffff;
  --soft:#f8f9fc;
  --ink:#1b2a4a;
  --muted:#8a93a3;
  --line:#c9ced6;
}
*{margin:0;padding:0;box-sizing:border-box}
html,body{width:1200px;height:4276px;overflow:hidden;background:var(--paper)}
body{font-family:"Work Sans",sans-serif;color:var(--ink);position:relative}
.abs{position:absolute}
.page{position:relative;width:1200px;height:4276px;overflow:hidden}

/* hero */
.hero-left{left:0;top:0;width:692px;height:652px;background:var(--navy)}
.hero-right{left:692px;top:0;width:508px;height:652px;background:linear-gradient(120deg,#eef2f4,#dfe6e9)}
.logo{left:61px;top:22px;font-family:"Oswald",sans-serif;font-weight:400;font-size:46px;letter-spacing:8px;color:#fff}
.nav{left:244px;top:38px;display:flex;gap:15px;font-size:12px;color:#fff;font-weight:500}
.nav .nav-label{color:var(--teal);font-weight:400;margin-right:-3px}
.nav .active{position:relative}
.nav .active::after{content:"";position:absolute;left:0;top:20px;width:16px;height:2px;background:#fff}
.menu{left:920px;top:34px;font-size:9px;letter-spacing:1px;color:var(--navy)}
.menu i{display:block;width:28px;height:6px;margin-top:3px;background:repeating-linear-gradient(90deg,var(--navy) 0 2px,transparent 2px 5px)}
.btn{display:inline-flex;align-items:center;justify-content:center;font-size:13px;font-weight:600}
.btn-yellow{background:var(--yellow);color:#fff}
.btn-outline{border:1px solid var(--yellow);color:var(--yellow);background:#fff}
.hero-request{left:980px;top:22px;width:160px;height:46px}
.side-rail{left:27px;width:1px;background:rgba(255,255,255,.3)}
.side-word{left:19px;font-size:11px;letter-spacing:1px;color:rgba(255,255,255,.45);transform:rotate(-90deg);transform-origin:left top;white-space:nowrap}
.hero-title{left:141px;top:152px;font-size:64px;font-weight:700;line-height:66px;color:#fff}
.hero-title .indent{padding-left:96px}
.hero-rule{left:141px;top:393px;width:345px;height:1px;background:rgba(255,255,255,.3)}
.hero-text{left:141px;top:416px;width:340px;font-size:10.5px;line-height:18px;color:#fff}
.hero-btn{left:141px;top:525px;width:161px;height:46px;border:1px solid var(--yellow);color:var(--yellow)}
.photo{display:block}
.dots{left:1124px;top:232px;display:flex;flex-direction:column;gap:26px;align-items:flex-end}
.dots span{display:block;width:4px;height:2px;background:var(--navy)}
.dots span:first-child{width:16px}
.entrance-link{left:996px;top:526px;width:52px;text-align:center;font-size:12px;color:var(--teal)}
.entrance-link::before{content:"";display:block;width:70px;height:1px;background:var(--teal);margin:0 0 22px -4px}

/* sections */
.rail{left:27px;width:1px;background:#e3e6ea}
.rail-word{left:21px;font-size:12px;letter-spacing:1px;color:#d3d7dd;transform:rotate(-90deg);transform-origin:left top;white-space:nowrap}
.eyebrow{left:153px;font-size:17px;line-height:21px;color:var(--teal-text);text-transform:uppercase}
.section-title{left:337px;width:640px;font-size:30px;line-height:36px;font-weight:600;color:var(--navy)}
.stat{width:240px}
.stat small{display:block;font-size:12px;color:#555}
.stat strong{display:block;font-family:"Oswald",sans-serif;font-weight:300;font-size:48px;color:var(--yellow);line-height:60px;margin-top:12px}
.stat span{display:block;font-size:13px;font-weight:500;color:#333;margin-top:8px}
.check{width:240px}
.check svg{display:block}
.check small{display:block;font-size:12px;color:#555;margin-top:24px}
.check span{display:block;font-size:13px;font-weight:500;color:#333;margin-top:12px;line-height:16px}
.rule{height:1px;background:#9aa1ab}
.body-copy{font-size:10.5px;line-height:18px;color:#6f7785}
.text-link{font-size:13px;color:var(--yellow);display:flex;align-items:center;gap:12px}
.text-link i{display:block;width:70px;height:1px;background:var(--yellow)}
.caption{font-size:9px;color:#777;transform:rotate(-90deg);transform-origin:left top;white-space:nowrap}

.types{left:0;top:3038px;width:1200px;height:941px;background:var(--soft)}
.type-card{top:3362px;width:161px;height:232px;background:#fff;border:1px solid #e3e6ea;text-align:center}
.type-card svg{margin-top:30px}
.type-card h3{font-size:18px;font-weight:500;color:var(--navy);margin-top:22px}
.type-card i{display:block;width:70px;height:1px;background:#f1d88a;margin:52px auto 0}

.contact{left:0;top:3979px;width:1200px;height:224px;background:var(--teal)}
.contact h2{position:absolute;left:60px;top:56px;font-size:30px;font-weight:600;color:#fff}
.contact .note{position:absolute;left:60px;top:118px;width:245px;font-size:10px;line-height:17px;color:#fff}
.contact .addr,.contact .hours{position:absolute;top:74px;font-size:18px;line-height:30px;color:#fff}
.contact .addr{left:335px}
.contact .hours{left:614px;display:grid;grid-template-columns:90px auto}
.contact-box{position:absolute;left:888px;top:45px;width:252px;height:131px;background:#fff;text-align:center;font-size:18px;font-weight:500;color:var(--navy);padding-top:36px;line-height:38px}
.footer{left:0;top:4203px;width:1200px;height:73px;background:var(--navy-deep);display:flex}
.footer a{flex:1;display:flex;align-items:center;justify-content:space-between;padding:0 24px 0 0;font-size:13px;font-weight:600;color:var(--yellow);text-decoration:none;border-right:1px solid rgba(255,255,255,.15)}
.footer a:first-child{padding-left:60px;flex:0 0 335px}
.footer a:not(:first-child){padding-left:0}
.footer a:nth-child(2){flex:0 0 279px}
.footer a:nth-child(3){flex:0 0 279px}
.footer a:last-child{border-right:0}
.footer a i{display:block;width:22px;height:1px;background:rgba(255,255,255,.6)}
</style>
</head>
<body>
<div class="page">

  <!-- hero -->
  <div class="abs hero-left"></div>
  <div class="abs hero-right"></div>
  <div class="abs side-rail" style="top:20px;height:110px"></div>
  <div class="abs side-word" style="top:245px">RELIABLY</div>
  <div class="abs side-word" style="top:325px">QUICKLY</div>
  <div class="abs side-word" style="top:455px">HIGH QUALITY</div>
  <div class="abs side-rail" style="top:500px;height:130px"></div>

  <div class="abs logo">LUM</div>
  <nav class="abs nav"><span class="nav-label">CLEANING:</span><span class="active">Office</span><span>Entrance</span><span>Building</span><span>Glass</span><span>Basic</span><span>Individual</span></nav>
  <div class="abs menu">MENU<i></i></div>
  <a class="abs btn btn-yellow hero-request">Request a cleaning</a>

  <div class="abs photo" role="img" aria-label="Bridge at dusk" style="left:377px;top:120px;width:78px;height:46px;background:linear-gradient(180deg,#c8a56a,#3a3f4a)"></div>
  <h1 class="abs hero-title">Office<br><span class="indent">cleaning</span><br>in Berlin</h1>
  <div class="abs photo" role="img" aria-label="Yellow taxi on a city street" style="left:141px;top:232px;width:77px;height:42px;background:linear-gradient(90deg,#5b5a56,#d6b23a,#3b3a38)"></div>
  <div class="abs photo" role="img" aria-label="Bright open-plan office with desks and red chairs" style="left:520px;top:120px;width:529px;height:351px;background:linear-gradient(180deg,#d9dcde 0%,#eef0f0 45%,#c9c4bd 100%)"></div>
  <div class="abs hero-rule"></div>
  <p class="abs hero-text">Lorem ipsum dolor sit amet, consectetur adipiscing elit. Purus duis faucibus vitae ac at vulputate quis. Et sit velit urna molestie libero diam pulvinar viverra amet. Nullam sit duis ultrices amet non, magna est massa. Sit sed purus urna, tellus malesuada sit.</p>
  <a class="abs btn hero-btn">Request a cleaning</a>
  <div class="abs photo" role="img" aria-label="Office tower windows lit at night" style="left:599px;top:516px;width:156px;height:97px;background:linear-gradient(90deg,#2a2414,#b08a2c 40%,#1e2636 70%,#8a94a4)"></div>
  <div class="abs dots"><span></span><span></span><span></span><span></span><span></span></div>
  <div class="abs entrance-link">Entrance</div>

  <!-- about -->
  <div class="abs rail" style="top:818px;height:110px"></div>
  <div class="abs rail-word" style="top:1030px">ABOUT US</div>
  <div class="abs rail" style="top:1060px;height:600px"></div>
  <div class="abs eyebrow" style="top:826px">Why you can<br>trust us</div>
  <h2 class="abs section-title" style="top:818px">Our work is hidden, but we are the support for your business. We free up time for important thoughts and actions.</h2>

  <div class="abs stat" style="left:339px;top:970px"><small>Experience</small><strong>20+</strong><span>since inception</span></div>
  <div class="abs stat" style="left:611px;top:970px"><small>We are</small><strong>85</strong><span>experienced employees</span></div>
  <div class="abs stat" style="left:888px;top:970px"><small>We are</small><strong>92%</strong><span>regular customers</span></div>

  <div class="abs check" style="left:339px;top:1137px"><svg width="54" height="40" viewBox="0 0 54 40"><path d="M3 20 L19 35 L51 3" fill="none" stroke="#ffd400" stroke-width="5"/></svg><small>Privacy:</small><span>no court cases</span></div>
  <div class="abs check" style="left:615px;top:1137px"><svg width="54" height="40" viewBox="0 0 54 40"><path d="M3 20 L19 35 L51 3" fill="none" stroke="#ffd400" stroke-width="5"/></svg><small>High quality:</small><span>only environmentally friendly<br>materials</span></div>
  <div class="abs check" style="left:890px;top:1137px"><svg width="54" height="40" viewBox="0 0 54 40"><path d="M3 20 L19 35 L51 3" fill="none" stroke="#ffd400" stroke-width="5"/></svg><small>Reliability:</small><span>cleaning of any complexity</span></div>

  <div class="abs photo" role="img" aria-label="Two businesswomen standing with arms crossed in an office" style="left:60px;top:1305px;width:528px;height:352px;background:linear-gradient(90deg,#e9ebec,#9a9ea6 40%,#cfd3d8 70%,#f1f2f3)"></div>
  <div class="abs rule" style="left:613px;top:1383px;width:526px"></div>
  <p class="abs body-copy" style="left:613px;top:1410px;width:526px">Lorem ipsum dolor sit amet, consectetur adipiscing elit. Purus duis faucibus vitae ac at vulputate quis. Et sit velit urna molestie libero diam pulvinar viverra amet. Nullam sit duis ultrices amet non, magna est massa. Sit sed purus urna, tellus malesuada sit. Lorem ipsum dolor sit amet, consectetur adipiscing elit. Purus duis faucibus vitae ac at vulputate quis. Et sit velit urna molestie libero diam pulvinar viverra amet. Nullam sit duis ultrices amet non, magna est massa. Sit sed purus urna, tellus malesuada sit.</p>
  <a class="abs btn btn-yellow" style="left:613px;top:1536px;width:99px;height:43px">About Us</a>
  <a class="abs text-link" style="left:727px;top:1548px">Benefits of long-term cooperation <i></i></a>

  <!-- work -->
  <div class="abs rail" style="top:1825px;height:110px"></div>
  <div class="abs rail-word" style="top:2038px">OUR WORK</div>
  <div class="abs rail" style="top:2070px;height:880px"></div>
  <div class="abs eyebrow" style="top:1832px">What can we do</div>
  <h2 class="abs section-title" style="top:1824px">Our most challenging projects. We are not afraid of difficulties. We are interested in overcoming them.</h2>

  <div class="abs rule" style="left:337px;top:1980px;width:251px"></div>
  <p class="abs body-copy" style="left:337px;top:2006px;width:251px">Lorem ipsum dolor sit amet, consectetur adipiscing elit. Purus duis faucibus vitae ac at vulputate quis. Et sit velit urna molestie libero diam pulvinar viverra amet. Nullam sit duis ultrices amet non, magna est massa. Sit sed purus urna, tellus malesuada sit. Lorem ipsum dolor sit amet, consectetur adipiscing elit. Purus duis faucibus vitae ac at vulputate quis. Et sit velit urna molestie libero diam pulvinar viverra amet. Nullam sit duis ultrices amet non, magna est massa. Sit sed purus urna, tellus malesuada sit.</p>
  <div class="abs photo" role="img" aria-label="Worker on ropes cleaning a glass facade at height" style="left:611px;top:1980px;width:529px;height:352px;background:linear-gradient(135deg,#8fa6b6,#c9d0d2 50%,#7e8c97)"></div>
  <div class="abs caption" style="left:598px;top:2332px">Work at height</div>

  <div class="abs photo" role="img" aria-label="Turquoise glass facade of a tower" style="left:60px;top:2332px;width:252px;height:170px;background:linear-gradient(135deg,#5fb8c4,#2a8fa2)"></div>
  <div class="abs caption" style="left:48px;top:2502px">Glass facade</div>
  <div class="abs photo" role="img" aria-label="Ferris wheel against a light blue sky" style="left:335px;top:2332px;width:253px;height:352px;background:linear-gradient(160deg,#e6f4f8,#8fd0e6 60%,#6fc2de)"></div>
  <div class="abs caption" style="left:324px;top:2684px">Ferris Wheel</div>

  <div class="abs rule" style="left:613px;top:2487px;width:526px"></div>
  <p class="abs body-copy" style="left:613px;top:2514px;width:526px">Lorem ipsum dolor sit amet, consectetur adipiscing elit. Purus duis faucibus vitae ac at vulputate quis. Et sit velit urna molestie libero diam pulvinar viverra amet. Nullam sit duis ultrices amet non, magna est massa. Sit sed purus urna, tellus malesuada sit. Lorem ipsum dolor sit amet, consectetur adipiscing elit. Purus duis faucibus vitae ac at vulputate quis. Et sit velit urna molestie libero diam pulvinar viverra amet. Nullam sit duis ultrices amet non, magna est massa. Sit sed purus urna, tellus malesuada sit.</p>
  <a class="abs btn btn-yellow" style="left:613px;top:2640px;width:127px;height:44px">Mehr Projects</a>
  <a class="abs btn btn-outline" style="left:752px;top:2640px;width:161px;height:44px">Request a cleaning</a>

  <div class="abs photo" role="img" aria-label="Bright multi-level library interior" style="left:151px;top:2708px;width:254px;height:167px;background:linear-gradient(180deg,#dcdfe2,#a7adb3 50%,#e9ebec)"></div>
  <div class="abs caption" style="left:140px;top:2875px">Library</div>

  <!-- types -->
  <div class="abs types"></div>
  <div class="abs rail" style="top:3060px;height:110px"></div>
  <div class="abs rail-word" style="top:3340px">THE TYPE OF CLEANING</div>
  <div class="abs rail" style="top:3370px;height:600px"></div>
  <div class="abs eyebrow" style="top:3218px">Choose the<br>type of<br>cleaning</div>
  <h2 class="abs section-title" style="top:3208px">Our most challenging projects. We are not afraid of difficulties. We are interested in overcoming them.</h2>

  <div class="abs type-card" style="left:60px"><svg width="60" height="60" viewBox="0 0 60 60" fill="none" stroke="#2ba8a8" stroke-width="2"><rect x="17" y="6" width="26" height="50"/><path d="M10 56h40"/><path d="M23 14h5v5h-5zM32 14h5v5h-5zM23 25h5v5h-5zM32 25h5v5h-5zM23 36h5v5h-5zM32 36h5v5h-5z"/><path d="M27 56v-8h6v8"/></svg><h3>Office</h3><i></i></div>
  <div class="abs type-card" style="left:244px"><svg width="60" height="60" viewBox="0 0 60 60" fill="none" stroke="#2ba8a8" stroke-width="2"><path d="M6 56h48M10 12h40v6H10zM14 18v38M46 18v38"/><rect x="20" y="22" width="20" height="34"/><path d="M30 22v34M26 38h2M32 38h2"/><path d="M25 6h10v6H25z"/></svg><h3>Entrance</h3><i></i></div>
  <div class="abs type-card" style="left:428px"><svg width="60" height="60" viewBox="0 0 60 60" fill="none" stroke="#2ba8a8" stroke-width="2"><rect x="22" y="8" width="28" height="48"/><path d="M26 14h4v4h-4zM34 14h4v4h-4zM42 14h4v4h-4zM26 24h4v4h-4zM34 24h4v4h-4zM42 24h4v4h-4zM26 34h4v4h-4zM34 34h4v4h-4zM42 34h4v4h-4z"/><path d="M6 56h50M13 56V44"/><ellipse cx="13" cy="38" rx="6" ry="9"/></svg><h3>Building</h3><i></i></div>
  <div class="abs type-card" style="left:612px"><svg width="60" height="60" viewBox="0 0 60 60" fill="none" stroke="#2ba8a8" stroke-width="2"><rect x="6" y="8" width="48" height="42"/><rect x="11" y="13" width="38" height="32"/><path d="M16 40l24-22M22 42l20-18M30 20l12 12M6 56h48"/></svg><h3>Glass</h3><i></i></div>
  <div class="abs type-card" style="left:795px"><svg width="60" height="60" viewBox="0 0 60 60" fill="none" stroke="#2ba8a8" stroke-width="2"><path d="M6 30L30 8l24 22M12 25v31h36V25"/><path d="M18 14V6h6v6"/><rect x="25" y="40" width="10" height="16"/><path d="M16 32h6v6h-6zM38 32h6v6h-6z"/></svg><h3>Basic</h3><i></i></div>
  <div class="abs type-card" style="left:979px"><svg width="60" height="60" viewBox="0 0 60 60" fill="none" stroke="#2ba8a8" stroke-width="2"><circle cx="30" cy="22" r="8"/><path d="M16 54V42a14 14 0 0 1 28 0v12"/><path d="M10 8v6M7 11h6M50 8v6M47 11h6" /><path d="M20 6l2 3M40 6l-2 3M30 4v3" stroke-dasharray="2 2"/></svg><h3>Individual</h3><i></i></div>

  <p class="abs body-copy" style="left:337px;top:3637px;width:518px">Lorem ipsum dolor sit amet, consectetur adipiscing elit. Purus duis faucibus vitae ac at vulputate quis. Et sit velit urna molestie libero diam pulvinar viverra amet. Nullam sit duis ultrices amet non, magna est massa. Sit sed purus urna, tellus malesuada sit. Lorem ipsum dolor sit amet, consectetur adipiscing elit. Purus duis faucibus vitae ac at vulputate quis. Et sit velit urna molestie libero diam pulvinar viverra amet. Nullam sit duis ultrices amet non, magna est massa. Sit sed purus urna, tellus malesuada sit.</p>
  <a class="abs btn btn-yellow" style="left:337px;top:3770px;width:159px;height:43px">Request a cleaning</a>
  <a class="abs btn btn-outline" style="left:505px;top:3770px;width:106px;height:43px">Contact us</a>

  <!-- contact -->
  <section class="abs contact">
    <h2>Contact</h2>
    <p class="note">If you would like to discuss your unusual assignment, you have suggestions for us, please contact us</p>
    <div class="addr">42 Karlsbader Ufer<br>Berlin<br>10785 Deutschland</div>
    <div class="hours"><span>MO - FR:</span><span>09:00 - 19:00</span><span>SA:</span><span>09:00 - 17:00</span><span>SU:</span><span>10:00 - 14:00</span></div>
    <div class="contact-box">+49 30 555 018 442<br>hallo@lum-reinigung.de</div>
  </section>
  <nav class="abs footer">
    <a>Long-term cooperation <i></i></a>
    <a>Guarantees <i></i></a>
    <a>About Us <i></i></a>
    <a>Vacancies <i></i></a>
  </nav>
</div>
</body>
</html>
```